Brochure Design Project - Innovative Service for Pharma Industry

Our start up is based in Germany, near Munich and we provide an innovative Service for the pharma industry. We develop product trainings and general trainings online. The adressed audience for these trainings are pharmacies and medics. The parma industry could increase the number of trainings, while saving money (incl a success guarantee). Our (not yet finnished) corporate page can be reviewed here: www.veltrano.biz, our 'product & service' page is www.medolearnix.com. The color code should be leaned towards the corporate page.

The brochure should be send to decision makers in the pharma industry and rise the interest in innovative service. Seriousity should meet modern & clear design.Something eye cathing on the front page might be required.
Updates

Target Market(s)

Usually more conservative decision makers within the pharma industry

Industry/Entity Type

Industry

Requirements
Must have
• Conceptional design for an brochure (Din A4 size) of approx 6-8 pages, that capture the key messages (exact content would be filled / provided from us)
Nice to have
• Implementing some of the pics / phrases on the home page www.veltano.biz could be maybe nice. How about a personal statement from the founder combined with a pic(pic attached)? Both is no must....

```html
<!DOCTYPE html>
<html lang="en">
<head>
<meta charset="utf-8">
<title>Veltrano – Content</title>
<link rel="stylesheet" href="https://fonts.googleapis.com/css2?family=Didact+Gothic&display=swap">
<style>
  :root {
    --accent: #e8461e;
    --ink: #5a5f66;
    --rule: #c8c8c8;
    --paper: #ffffff;
  }
  html, body {
    margin: 0;
    padding: 0;
    overflow: hidden;
    background: var(--paper);
  }
  .page {
    position: relative;
    width: 1200px;
    height: 908px;
    overflow: hidden;
    background: var(--paper);
    font-family: "Didact Gothic", "Century Gothic", sans-serif;
    color: var(--ink);
  }
  .brand-name {
    position: absolute;
    right: 90px;
    top: 224px;
    font-size: 40px;
    line-height: 48px;
    letter-spacing: 1px;
    color: var(--ink);
  }
  .toc-rule-v {
    position: absolute;
    left: 154px;
    top: 393px;
    width: 1px;
    height: 380px;
    background: var(--rule);
  }
  .toc-rule-h {
    position: absolute;
    left: 90px;
    top: 487px;
    width: 630px;
    height: 1px;
    background: var(--rule);
  }
  .toc {
    position: absolute;
    left: 213px;
    top: 425px;
    width: 478px;
    margin: 0;
    padding: 0;
    list-style: none;
  }
  .toc-row {
    display: flex;
    justify-content: space-between;
    align-items: center;
  }
  .toc-title {
    height: 52px;
    font-size: 44px;
    line-height: 52px;
    color: var(--accent);
    margin-bottom: 19px;
  }
  .toc-title .toc-page {
    font-size: 20px;
    color: var(--ink);
    padding-top: 4px;
  }
  .toc-item {
    height: 51px;
    font-size: 23px;
    line-height: 51px;
    color: var(--ink);
  }
  .toc-item .toc-page { font-size: 20px; }
  .folio {
    position: absolute;
    right: 72px;
    top: 822px;
    font-size: 21px;
    line-height: 28px;
    color: var(--ink);
  }
</style>
</head>
<body>
<main class="page">
  <header class="brand-name">Veltrano</header>

  <div class="toc-rule-v"></div>
  <div class="toc-rule-h"></div>

  <ul class="toc">
    <li class="toc-row toc-title"><span>Content</span><span class="toc-page">2</span></li>
    <li class="toc-row toc-item"><span>About Us</span><span class="toc-page">4</span></li>
    <li class="toc-row toc-item"><span>Our Services</span><span class="toc-page">5</span></li>
    <li class="toc-row toc-item"><span>Products</span><span class="toc-page">7</span></li>
    <li class="toc-row toc-item"><span>Contact</span><span class="toc-page">9</span></li>
  </ul>

  <div class="folio">2</div>
</main>
</body>
</html>
```